Corvane spray foam and Environmental

I have business cards but need new ones. The ones I have are very bland. Here is. Y company website http://www.corvanesprayfoam.ca

Also I can send you copies of the current cards
I would also need my current logo on the new design as well.. Also spray foam and Environmental

Industry/Entity Type

Business

Logo Text

Corvane.

```html
<!DOCTYPE html>
<html lang="en">
<head>
<meta charset="utf-8">
<title>Corvane Business Cards</title>
<link rel="stylesheet" href="https://fonts.googleapis.com/css2?family=Roboto:wght@400;500&family=Montserrat:wght@800&display=swap">
<style>
  :root {
    --purple: #5b2d8a;
    --purple-text: #6a3596;
    --grey-band: #6b6869;
    --green: #7cc12a;
    --text: #555558;
    --card: #ffffff;
    --backdrop: #e4e4e4;
  }
  * { box-sizing: border-box; margin: 0; padding: 0; }
  html, body { width: 1200px; height: 852px; overflow: hidden; }
  body {
    background: var(--backdrop);
    font-family: "Roboto", Arial, sans-serif;
    position: relative;
  }
  .card {
    position: absolute;
    width: 525px;
    height: 300px;
    background: var(--card);
    border-radius: 22px;
    overflow: hidden;
    box-shadow: 0 6px 18px rgba(0,0,0,0.18);
  }
  .card--foam { left: 70px; top: 110px; }
  .card--enviro { left: 605px; top: 440px; }

  .brand {
    position: absolute;
    left: 40px;
    top: 96px;
    width: 210px;
  }
  .brand__mark {
    width: 26px; height: 26px;
    background: var(--purple);
    border-radius: 5px;
    margin-bottom: 14px;
  }
  .brand__name {
    font-family: "Montserrat", Arial, sans-serif;
    font-weight: 800;
    font-size: 20px;
    line-height: 1.15;
    color: var(--purple);
    text-transform: uppercase;
    white-space: nowrap;
  }

  .contact {
    position: absolute;
    left: 272px;
    top: 44px;
    list-style: none;
    font-size: 13px;
    color: var(--text);
  }
  .contact li { display: flex; align-items: center; gap: 10px; height: 19px; }
  .contact svg { width: 12px; height: 12px; fill: none; stroke: var(--purple); stroke-width: 1.6; }
  .contact .web { color: var(--purple-text); }

  .services {
    position: absolute;
    left: 286px;
    top: 122px;
    display: flex;
    gap: 14px;
    font-size: 11px;
    color: var(--text);
  }
  .services ul { list-style: none; }
  .services li { line-height: 15px; white-space: nowrap; }
  .services li::before { content: "» "; color: var(--purple); }
  .card--enviro .services li::before { color: var(--green); }
  .card--enviro .services ul + ul { align-self: flex-end; }

  .base-strip {
    position: absolute; left: 0; right: 0; bottom: 0;
    height: 10px; background: var(--purple);
  }
  .tagline-band {
    position: absolute; right: 0; bottom: 0;
    width: 220px; height: 52px;
    border-top-left-radius: 16px;
    display: flex; align-items: center; justify-content: center;
    color: #fff; font-size: 13px;
  }
  .card--foam .tagline-band { background: var(--grey-band); }
  .card--enviro .tagline-band { background: var(--green); }
</style>
</head>
<body>

<article class="card card--foam">
  <div class="brand">
    <div class="brand__mark"></div>
    <div class="brand__name">Corvane<br>Spray Foam</div>
  </div>
  <ul class="contact">
    <li><svg viewBox="0 0 12 12"><circle cx="6" cy="6" r="5"/><path d="M4 3.5l1 1.5-.6.6a3 3 0 002 2l.6-.6 1.5 1"/></svg>604-555-0148</li>
    <li><svg viewBox="0 0 12 12"><rect x="1" y="2.5" width="10" height="7"/><path d="M1 2.5l5 4 5-4"/></svg>corvanefoam@gmail.com</li>
    <li><svg viewBox="0 0 12 12"><circle cx="6" cy="6" r="5"/><path d="M1 6h10M6 1c2.5 3 2.5 7 0 10M6 1c-2.5 3-2.5 7 0 10"/></svg><span>www.<span class="web">corvanesprayfoam</span>.ca</span></li>
  </ul>
  <div class="services">
    <ul>
      <li>Roofing Foam</li>
      <li>2 Pound / Half Pound</li>
      <li>Sound Proofing</li>
      <li>Batt Insulation</li>
    </ul>
    <ul>
      <li>Slab Jacking</li>
      <li>Attic Blow in</li>
    </ul>
  </div>
  <div class="base-strip"></div>
  <div class="tagline-band">Residential and Commercial</div>
</article>

<article class="card card--enviro">
  <div class="brand">
    <div class="brand__mark"></div>
    <div class="brand__name">Corvane<br>Environmental</div>
  </div>
  <ul class="contact">
    <li><svg viewBox="0 0 12 12"><circle cx="6" cy="6" r="5"/><path d="M4 3.5l1 1.5-.6.6a3 3 0 002 2l.6-.6 1.5 1"/></svg>604-555-0193</li>
    <li><svg viewBox="0 0 12 12"><rect x="1" y="2.5" width="10" height="7"/><path d="M1 2.5l5 4 5-4"/></svg>corvaneenviro1@gmail.com</li>
    <li><svg viewBox="0 0 12 12"><circle cx="6" cy="6" r="5"/><path d="M1 6h10M6 1c2.5 3 2.5 7 0 10M6 1c-2.5 3-2.5 7 0 10"/></svg><span class="web">corvaneenvironmental.ca</span></li>
  </ul>
  <div class="services">
    <ul>
      <li>Air Monitoring</li>
      <li>Asbestos Testing</li>
      <li>Asbestos Removal</li>
      <li>Building Demolition</li>
      <li>Lead Testing</li>
    </ul>
    <ul>
      <li>Mould Removal</li>
    </ul>
  </div>
  <div class="base-strip"></div>
  <div class="tagline-band">Residential and Commercial</div>
</article>

</body>
</html>
```